Billboard Design for Modern Dispensary

Hello!
We need a eye-catching 12' x 24' billboard designed for a very successful, modern cannabis dispensary on the Oregon coast, United States. Because of rules, we cannot have any marijuana leafs or other cannabis related images (flower, joints, smoke, etc). We can use the words "Shop" or "Dispensary" - we cannot use the words "cannabis", "marijuana".

Some ideas we had are 3 words stacked on left or center of billboard - maybe across bottom we have horizontal logo and the following words - “South of bridge in Tern Cove”
Another idea is to have a small bubble in bottom/top corner with image of our dog (face only) - with some words around it - like "BONUS Shop Dog" or "Cute Shop Dog" or "Best Shop Dog" or "Friendly Staff"

here's some 3 word examples:
ENJOY
YOUR
TRIP

or

FEEL
GOOD
JUST
AHEAD

or

GOOD
VIBES
ONLY

or

GOOD
TIMES
CHILL
VIBES

I have attached our logo. I have also included a stacked logo version (vertical, not horizontal). the formats are .EPS and .PDF - the logos were created in Affinity Design 2.x.

Our website is coralnook.net if you want to see more images, etc about our dispensary.

Artwork Requirements:
The billboard is 12' tall x 25' wide
The artwork needs to be 1”=1’ @ 300dpi
Please add 6” of bleed all around so your total artwork is 13”x26”
Final deliverable should be .Ai file.

Font styles to use
Sans Serif

Colors
0054AA
0677BA
7BADD7
CADEEF
E8F1F8

Requirements
Nice to have
• See the project description - we included some ideas to consider.
Should not have
• No cannabis images, like flower, cannabis leaves, paraphenlia, cartridges, joints, etc.

```html
<!DOCTYPE html>
<html lang="en">
<head>
<meta charset="utf-8">
<title>Coral Nook Billboard</title>
<link rel="stylesheet" href="https://fonts.googleapis.com/css2?family=Roboto+Condensed:wght@400;700;800&display=swap">
<style>
  :root {
    --stage: #777777;
    --board: #ffffff;
    --brand-blue: #3b9ad6;
    --ink: #0b0b0b;
    --ink-soft: #222222;
    --photo-light: #d8b98a;
    --photo-dark: #6b4e3a;
  }
  html, body {
    margin: 0;
    padding: 0;
    width: 1199px;
    height: 1200px;
    overflow: hidden;
    background: var(--stage);
  }
  .billboard {
    position: absolute;
    left: 0;
    top: 300px;
    width: 1199px;
    height: 600px;
    display: block;
  }
  .board-bg { fill: var(--board); }
  .band-blue { fill: var(--brand-blue); }
  .wedge-black { fill: var(--ink); }
  .brand-dot { fill: none; stroke: var(--brand-blue); stroke-width: 4; }
  .brand-name {
    font-family: "Roboto Condensed", sans-serif;
    font-weight: 400;
    font-size: 30px;
    fill: var(--brand-blue);
  }
  .brand-place {
    font-family: "Roboto Condensed", sans-serif;
    font-weight: 400;
    font-size: 8.5px;
    letter-spacing: 4px;
    fill: var(--ink-soft);
  }
  .brand-rule { stroke: var(--ink-soft); stroke-width: 0.8; }
  .headline {
    font-family: "Roboto Condensed", sans-serif;
    font-weight: 800;
    font-size: 54px;
    fill: var(--ink);
  }
  .location {
    font-family: "Roboto Condensed", sans-serif;
    font-weight: 700;
    font-size: 32px;
    fill: var(--board);
  }
  .photo-frame { fill: var(--board); }
</style>
</head>
<body>
<svg class="billboard" viewBox="0 0 760 380" xmlns="http://www.w3.org/2000/svg">
  <defs>
    <radialGradient id="photoTone" cx="45%" cy="45%" r="60%">
      <stop offset="0%" stop-color="#d8b98a"/>
      <stop offset="100%" stop-color="#6b4e3a"/>
    </radialGradient>
  </defs>

  <rect class="board-bg" x="0" y="0" width="760" height="380"/>

  <g class="brand">
    <circle class="brand-dot" cx="78" cy="71" r="30"/>
    <text class="brand-name" x="116" y="75" textLength="167" lengthAdjust="spacingAndGlyphs">CORAL NOOK</text>
    <line class="brand-rule" x1="118" y1="88" x2="148" y2="88"/>
    <text class="brand-place" x="156" y="91" textLength="94">TERN COVE</text>
    <line class="brand-rule" x1="257" y1="88" x2="287" y2="88"/>
  </g>

  <polygon class="wedge-black" points="297,106 222,166 242,380"/>
  <polygon class="band-blue" points="297,106 760,219 760,380 242,380"/>

  <g class="headline-stack">
    <text class="headline" x="47" y="207" textLength="118" lengthAdjust="spacingAndGlyphs">SLEEP</text>
    <text class="headline" x="47" y="270" textLength="140" lengthAdjust="spacingAndGlyphs">BETTER</text>
    <text class="headline" x="47" y="332" textLength="164" lengthAdjust="spacingAndGlyphs">TONIGHT</text>
  </g>

  <g class="shop-dog">
    <circle class="photo-frame" cx="521" cy="159" r="115"/>
    <circle cx="521" cy="159" r="110" fill="url(#photoTone)" role="img" aria-label="Photo of the shop dog, a smiling golden doodle wearing a bandana"/>
  </g>

  <text class="location" x="300" y="334">South of bridge in Tern Cove</text>
</svg>
</body>
</html>
```